Real Estate Agent needs business card design

We have logo designed already, want to have business card designed. Very interested in those smaller size business card as they look very trendy. Business name is called TOVANE REALTY

Industry/Entity Type

Business

```html
<!DOCTYPE html>
<html lang="en">
<head>
<meta charset="utf-8">
<title>Tovane Realty – Business Card</title>
<link rel="stylesheet" href="https://fonts.googleapis.com/css2?family=Tinos:wght@400;700&display=swap">
<style>
  :root {
    --gold: #c9a26c;
    --ink: #2b2a2d;
    --paper: #ffffff;
    --backdrop: #e9e7e4;
    --serif: "Tinos", "Times New Roman", serif;
  }
  * { margin: 0; padding: 0; box-sizing: border-box; }
  html, body { width: 1200px; height: 900px; overflow: hidden; }
  body { background: var(--backdrop); position: relative; font-family: var(--serif); }

  .card {
    position: absolute;
    width: 620px;
    height: 380px;
    border-radius: 26px;
    overflow: hidden;
    box-shadow: 0 10px 28px rgba(0,0,0,0.18);
  }
  .card--back { left: 500px; top: 50px; background: var(--gold); }
  .card--front { left: 80px; top: 470px; background: var(--paper); }

  .brand-name {
    position: absolute;
    font-family: var(--serif);
    font-variant: small-caps;
    letter-spacing: 1px;
    white-space: nowrap;
  }
  .card--back .brand-name { left: 44px; top: 150px; font-size: 26px; color: var(--paper); }
  .card--front .brand-name { left: 60px; top: 80px; font-size: 38px; color: var(--ink); }

  .wave { position: absolute; inset: 0; width: 100%; height: 100%; }

  .address {
    position: absolute; left: 60px; top: 138px;
    font-size: 15px; line-height: 1.3; color: var(--ink);
  }
  .agent { position: absolute; right: 44px; top: 118px; text-align: right; }
  .agent__name { font-size: 24px; font-variant: small-caps; letter-spacing: 1px; color: var(--ink); }
  .agent__role { font-size: 16px; color: var(--gold); margin-top: 2px; }

  .contacts {
    position: absolute; right: 30px; top: 292px;
    list-style: none; font-size: 16px; color: var(--ink);
  }
  .contacts li { display: flex; align-items: center; justify-content: flex-end; gap: 10px; height: 25px; }
  .contacts svg { width: 17px; height: 17px; fill: var(--ink); }
</style>
</head>
<body>

  <section class="card card--back" aria-label="Card back">
    <p class="brand-name">Tovane Realty</p>
  </section>

  <section class="card card--front" aria-label="Card front">
    <svg class="wave" viewBox="0 0 620 380" preserveAspectRatio="none" aria-hidden="true">
      <path d="M0,128 C140,175 300,208 470,228 C540,238 590,262 620,282 L620,286 C580,268 520,250 440,240 C280,225 130,190 0,150 Z" fill="var(--gold)"/>
      <path d="M0,158 C120,210 300,222 470,248 C530,258 575,272 600,288 C560,276 500,266 430,258 C270,242 110,222 0,178 Z" fill="var(--ink)"/>
      <path d="M0,200 C130,250 320,230 470,262 C545,278 590,290 620,300 L620,380 L0,380 Z" fill="var(--gold)"/>
    </svg>

    <p class="brand-name">Tovane Realty</p>

    <address class="address" style="font-style:normal">
      7C, 48 Harbour Street<br>
      Milsons Point, NSW 2061
    </address>

    <div class="agent">
      <p class="agent__name">Ellen Marsh</p>
      <p class="agent__role">Senior Property Consultant</p>
    </div>

    <ul class="contacts">
      <li>0412 555 180
        <svg viewBox="0 0 24 24" aria-hidden="true"><path d="M6.6 10.8a15 15 0 0 0 6.6 6.6l2.2-2.2c.3-.3.7-.4 1-.2 1.1.4 2.3.6 3.6.6.6 0 1 .4 1 1V20c0 .6-.4 1-1 1A17 17 0 0 1 3 4c0-.6.4-1 1-1h3.5c.6 0 1 .4 1 1 0 1.3.2 2.5.6 3.6.1.3 0 .7-.2 1z"/></svg>
      </li>
      <li>tovanerealty@email.com
        <svg viewBox="0 0 24 24" aria-hidden="true"><path d="M2 5h20v14H2z M4 7v.5l8 5 8-5V7l-8 5z" fill-rule="evenodd"/></svg>
      </li>
      <li>www.tovanerealty.com.au
        <svg viewBox="0 0 24 24" aria-hidden="true"><path d="M12 2a10 10 0 1 0 0 20 10 10 0 0 0 0-20zm6.9 6h-3a15 15 0 0 0-1.3-3.9A8 8 0 0 1 18.9 8zM12 4c.8 1.2 1.5 2.5 1.9 4h-3.8c.4-1.5 1.1-2.8 1.9-4zM4.3 14a8 8 0 0 1 0-4h3.4a16 16 0 0 0 0 4zm.8 2h3a15 15 0 0 0 1.3 3.9A8 8 0 0 1 5.1 16zm3-8h-3a8 8 0 0 1 4.3-3.9A15 15 0 0 0 8.1 8zM12 20c-.8-1.2-1.5-2.5-1.9-4h3.8c-.4 1.5-1.1 2.8-1.9 4zm2.3-6H9.7a14 14 0 0 1 0-4h4.6a14 14 0 0 1 0 4zm.3 5.9a15 15 0 0 0 1.3-3.9h3a8 8 0 0 1-4.3 3.9zm1.7-5.9a16 16 0 0 0 0-4h3.4a8 8 0 0 1 0 4z"/></svg>
      </li>
    </ul>
  </section>

</body>
</html>
```